Logo redesign & Stationery Design Project

We need a logo redesign for our company.

We also require the following stationary with the new logo:
*letterhead
*With compliments slips
*business card
*envelopes

We would like to maintain our current colours of navy blue and gold. We would like to maintain the wording on the back of our current business card.

Our existing letterhead and business card is attached.

Target Market(s)

Medical Professionals, Pharmacists, Lawyers

Industry/Entity Type

Business

Requirements
Must have
• See attached business card and letterhead, as all details on these documents need to be included.

```html
<!DOCTYPE html>
<html lang="en">
<head>
<meta charset="utf-8">
<title>Halden Marsh Financial Services – Stationery</title>
<link href="https://fonts.googleapis.com/css2?family=Questrial&family=Arimo:wght@400&display=swap" rel="stylesheet">
<style>
  :root {
    --navy: #1f2c68;
    --gold: #a8955f;
    --gold-light: #b9a872;
    --paper: #ffffff;
    --paper-soft: #f3f3f3;
    --ink: #222222;
    --stage: #d9dadc;
    --brand-font: "Questrial", "Century Gothic", sans-serif;
    --body-font: "Arimo", Arial, sans-serif;
  }
  * { box-sizing: border-box; margin: 0; padding: 0; }
  html, body { width: 1200px; height: 900px; overflow: hidden; }
  body { background: var(--stage); font-family: var(--brand-font); position: relative; }

  .sheet { position: absolute; background: var(--paper); box-shadow: 0 3px 10px rgba(0,0,0,.25); overflow: hidden; }

  /* brand lockup */
  .brand { display: flex; align-items: center; gap: 10px; }
  .brand-dot { border-radius: 50%; background: var(--gold); flex: none; }
  .brand-name { font-family: var(--brand-font); color: var(--gold); line-height: 1; white-space: nowrap; }
  .brand-name span { display: block; }
  .brand-navy .brand-dot { background: var(--navy); }
  .brand-navy .brand-name { color: var(--navy); }

  .contact { font-family: var(--brand-font); color: #e6e3d6; line-height: 1.3; white-space: nowrap; }
  .rule-pair { position: absolute; }
  .rule-pair::before, .rule-pair::after { content: ""; display: block; height: 3px; }
  .rule-pair::before { background: var(--navy); margin-bottom: 2px; }
  .rule-pair::after { background: var(--gold); }

  /* letterhead */
  .letterhead { left: 40px; top: 30px; width: 430px; height: 840px; }
  .letterhead .header { position: absolute; left: 0; top: 0; width: 100%; height: 100px; background: var(--navy); border-bottom: 4px solid var(--gold); }
  .letterhead .brand { position: absolute; left: 20px; top: 30px; }
  .letterhead .brand-dot { width: 40px; height: 40px; }
  .letterhead .brand-name { font-size: 20px; }
  .letterhead .brand-name span + span { font-size: 14px; margin-top: 2px; }
  .letterhead .contact { position: absolute; right: 18px; top: 22px; font-size: 9px; }
  .letter-body { position: absolute; left: 34px; right: 34px; top: 132px; font-family: var(--body-font); font-size: 9.5px; color: var(--ink); line-height: 1.45; }
  .letter-body p { margin-bottom: 11px; }
  .signature { width: 140px; height: 44px; margin: 8px 0 4px; background: linear-gradient(90deg, #e9e9e9, #f6f6f6); }
  .signer { margin-left: 110px; }
  .letterhead .footer-web { position: absolute; right: 22px; bottom: 40px; font-size: 12px; color: var(--navy); }
  .letterhead .rule-pair { left: 0; right: 0; bottom: 22px; }
  .letterhead .footer-note { position: absolute; left: 22px; bottom: 8px; font-size: 7.5px; color: var(--navy); }

  /* business cards */
  .card { top: 30px; width: 300px; height: 160px; }
  .card-front { left: 510px; background: var(--navy); }
  .card-front .brand { position: absolute; left: 18px; top: 32px; }
  .card-front .brand-dot { width: 30px; height: 30px; }
  .card-front .brand-name { font-size: 15px; }
  .card-front .brand-name span + span { font-size: 11px; margin-top: 2px; }
  .card-front .person { position: absolute; right: 16px; top: 38px; text-align: right; color: #fff; font-size: 9.5px; }
  .card-front .person small { display: block; color: var(--gold-light); font-size: 8px; margin-top: 2px; }
  .card-front .contact { position: absolute; left: 18px; top: 92px; font-size: 8px; }
  .card-front .card-web { position: absolute; right: 16px; bottom: 22px; font-size: 8px; color: #c9c6ba; }
  .card-front .rule { position: absolute; left: 18px; right: 120px; bottom: 24px; height: 2px; background: #fff; }
  .card-front .rule + .rule { bottom: 20px; background: var(--gold); }
  .card-back { left: 850px; background: var(--gold); }
  .card-back .brand { position: absolute; left: 50px; top: 52px; }
  .card-back .brand-dot { width: 40px; height: 40px; }
  .card-back .brand-name { font-size: 22px; }
  .card-back .brand-name span + span { font-size: 15px; margin-top: 3px; }
  .card-back .rule-pair { left: 0; right: 0; bottom: 10px; }
  .card-back .rule-pair::before { background: #fff; }
  .card-back .rule-pair::after { background: var(--navy); }

  /* envelope */
  .envelope { left: 510px; top: 210px; width: 640px; height: 220px; background: var(--paper-soft); }
  .envelope .header { position: absolute; left: 0; top: 0; width: 100%; height: 80px; background: var(--navy); border-bottom: 4px solid var(--gold); }
  .envelope .brand { position: absolute; left: 22px; top: 19px; }
  .envelope .brand-dot { width: 40px; height: 40px; }
  .envelope .brand-name { font-size: 21px; }
  .envelope .brand-name span + span { font-size: 14px; margin-top: 2px; }
  .envelope .contact { position: absolute; right: 22px; top: 22px; font-size: 9.5px; }
  .envelope .window { position: absolute; left: 40px; top: 104px; width: 220px; height: 72px; border-radius: 10px; background: #e4e4e4; }
  .envelope .env-web { position: absolute; right: 24px; bottom: 40px; font-size: 14px; color: var(--navy); }
  .envelope .rule-pair { left: 0; right: 0; bottom: 22px; }

  /* compliments slip with header band */
  .slip { left: 510px; width: 640px; }
  .slip-top { top: 450px; height: 195px; }
  .slip-top .header { position: absolute; left: 0; top: 0; width: 100%; height: 78px; background: var(--navy); border-bottom: 4px solid var(--gold); }
  .slip-top .brand { position: absolute; left: 22px; top: 19px; }
  .slip-top .brand-dot { width: 38px; height: 38px; }
  .slip-top .brand-name { font-size: 20px; }
  .slip-top .brand-name span + span { font-size: 13px; margin-top: 2px; }
  .slip-top .contact { position: absolute; right: 22px; top: 8px; font-size: 8.5px; }
  .slip-top .footer-note { position: absolute; left: 22px; bottom: 36px; font-size: 7.5px; color: var(--navy); }
  .slip-top .rule-pair { left: 0; right: 180px; bottom: 24px; }
  .slip-top .greeting { position: absolute; right: 22px; bottom: 20px; font-size: 15px; color: var(--navy); }

  /* compliments slip with side band */
  .slip-side { top: 665px; height: 205px; }
  .slip-side .side-band { position: absolute; left: 0; top: 0; bottom: 0; width: 90px; background: var(--navy); border-right: 4px solid var(--gold); }
  .slip-side .brand { position: absolute; left: 0; right: 0; bottom: 14px; flex-direction: column-reverse; gap: 10px; }
  .slip-side .brand-dot { width: 36px; height: 36px; }
  .slip-side .brand-name { font-size: 20px; writing-mode: vertical-rl; transform: rotate(180deg); }
  .slip-side .brand-name span + span { font-size: 13px; margin-left: 2px; }
  .slip-side .contact { position: absolute; right: 22px; top: 58px; font-size: 8.5px; color: var(--navy); text-align: right; }
  .slip-side .footer-note { position: absolute; right: 22px; bottom: 40px; font-size: 7.5px; color: var(--navy); }
  .slip-side .rule-pair { left: 300px; right: 0; bottom: 26px; }
  .slip-side .greeting { position: absolute; left: 116px; bottom: 18px; font-size: 15px; color: var(--navy); }
</style>
</head>
<body>

<section class="sheet letterhead" aria-label="Letterhead">
  <header class="header">
    <div class="brand"><span class="brand-dot"></span><div class="brand-name"><span>Halden Marsh</span><span>Financial Services</span></div></div>
    <div class="contact">Suite 4, 118 Harbour Road, Westbrook NSW 2190<br>PO Box 3321 Westbrook NSW 2190<br>t: 02 9000 1234 f: 02 9000 1235<br>e: dan@haldenmarsh.com.au</div>
  </header>
  <div class="letter-body">
    <p>Dear Client,</p>
    <p>Lorem ipsum dolor sit amet, consectetur adipisicing elit, sed do eiusmod tempor incididunt ut labore et dolore magna aliqua. Ut enim ad minim veniam, quis nostrud exercitation ullamco laboris nisi ut aliquip ex ea commodo consequat. Duis aute irure dolor in reprehenderit in voluptate velit esse cillum dolore eu fugiat nulla pariatur. Excepteur sint occaecat cupidatat non proident, sunt in culpa qui officia deserunt mollit anim id est laborum.</p>
    <p>Lorem ipsum dolor sit amet, consectetur adipisicing elit, sed do eiusmod tempor incididunt ut labore et dolore magna aliqua. Ut enim ad minim veniam, quis nostrud exercitation ullamco laboris nisi ut aliquip ex ea commodo consequat. Duis aute irure dolor in reprehenderit in voluptate velit esse cillum dolore eu fugiat nulla pariatur. Excepteur sint occaecat cupidatat non proident, sunt in culpa qui officia deserunt mollit anim id est laborum.</p>
    <p>Lorem ipsum dolor sit amet, consectetur adipisicing elit, sed do eiusmod tempor incididunt ut labore et dolore magna aliqua. Ut enim ad minim veniam, quis nostrud exercitation ullamco laboris nisi ut aliquip ex ea commodo consequat. Duis aute irure dolor in reprehenderit in voluptate velit esse cillum dolore eu fugiat nulla pariatur. Excepteur sint occaecat cupidatat non proident.</p>
    <p>Lorem ipsum dolor sit amet, consectetur adipisicing elit, sed do eiusmod tempor incididunt ut labore et dolore magna aliqua. Ut enim ad minim veniam, quis nostrud exercitation ullamco laboris nisi ut aliquip ex ea commodo consequat. Duis aute irure dolor in reprehenderit in voluptate velit esse cillum dolore eu fugiat nulla pariatur.</p>
    <p>Yours Sincerely,</p>
    <div class="signature" role="img" aria-label="Handwritten signature"></div>
    <p class="signer">Mark Ellison<br>Executive manager</p>
  </div>
  <div class="footer-web">www.haldenmarsh.com.au</div>
  <div class="rule-pair"></div>
  <div class="footer-note">Corporate Authorised Representative of Northgate Advisory Group AFSL 000000</div>
</section>

<section class="sheet card card-front" aria-label="Business card front">
  <div class="brand"><span class="brand-dot"></span><div class="brand-name"><span>Halden Marsh</span><span>Financial Services</span></div></div>
  <div class="person">Daniel (Dan) Okoro<small>Partner</small></div>
  <div class="contact">Suite 4, 118 Harbour Road, Westbrook<br>t: 02 9000 1234 m: 0400 000 123<br>e: dan@haldenmarsh.com.au</div>
  <div class="rule"></div><div class="rule"></div>
  <div class="card-web">www.haldenmarsh.com.au</div>
</section>

<section class="sheet card card-back" aria-label="Business card back">
  <div class="brand brand-navy"><span class="brand-dot"></span><div class="brand-name"><span>Halden Marsh</span><span>Financial Services</span></div></div>
  <div class="rule-pair"></div>
</section>

<section class="sheet envelope" aria-label="Envelope">
  <header class="header">
    <div class="brand"><span class="brand-dot"></span><div class="brand-name"><span>Halden Marsh</span><span>Financial Services</span></div></div>
    <div class="contact">Suite 4, 118 Harbour Road, Westbrook<br>t: 02 9000 1234 m: 0400 000 123<br>e: dan@haldenmarsh.com.au</div>
  </header>
  <div class="window"></div>
  <div class="env-web">www.haldenmarsh.com.au</div>
  <div class="rule-pair"></div>
</section>

<section class="sheet slip slip-top" aria-label="With compliments slip">
  <header class="header">
    <div class="brand"><span class="brand-dot"></span><div class="brand-name"><span>Halden Marsh</span><span>Financial Services</span></div></div>
    <div class="contact">Suite 4, 118 Harbour Road, Westbrook NSW 2190<br>PO Box 3321 Westbrook NSW 2190<br>t: 02 9000 1234 f: 02 9000 1235<br>e: admin@haldenmarsh.com.au<br>www.haldenmarsh.com.au</div>
  </header>
  <div class="footer-note">Corporate Authorised Representative of Northgate Advisory Group AFSL 000000</div>
  <div class="rule-pair"></div>
  <div class="greeting">With Compliments</div>
</section>

<section class="sheet slip slip-side" aria-label="With compliments slip, side band">
  <aside class="side-band">
    <div class="brand"><span class="brand-dot"></span><div class="brand-name"><span>Halden Marsh</span><span>Financial Services</span></div></div>
  </aside>
  <div class="contact">Suite 4, 118 Harbour Road, Westbrook NSW 2190<br>PO Box 3321 Westbrook NSW 2190<br>t: 02 9000 1234 f: 02 9000 1235<br>e: admin@haldenmarsh.com.au<br>www.haldenmarsh.com.au</div>
  <div class="footer-note">Corporate Authorised Representative of Northgate Advisory Group AFSL 000000</div>
  <div class="rule-pair"></div>
  <div class="greeting">With Compliments</div>
</section>

</body>
</html>
```